Packaging design for high end, natural skin care line needed

Marisol Thackery Beauty needs a label design. It is a new skin care line I am launching.
For years my line Velvet Orchard Beauty was quite popular and featured in several magazines, but for personal reasons had to be shut down. Now I am launching a new line featuring VOB's top selling products, but focused solely on skin care more so than cosmetics. All products will still be handmade, but the line should still look professional-something worthy of a Brindle Market shelf!
I am branding it with my name, as I am often quoted in articles related to gluten in beauty products, so Marisol Thackery and beauty are key words.
The key products will be facial and body serums which are packaged in .5oz., 1oz. and larger amber glass bottles with black dropper tops, I will include pictures below. For dimensions, the labels can be any size that you think will work best, but need to at the least fit the 1oz. bottle, dimensions shown here http://www.corvelflask.example/amber-glass-tall-round-flask/p/QZ7K-93/
I loved the former VOB logo, but for Marisol Thackery Beauty I am looking for something more personal, more apothecary-like, and probably less colorful.
The line will be small, just a handful of products, but luxe, rich.
I am attaching photos of Velvet Orchard Beauty's packaging for your reference.
Thanks much!!

Hi Everyone! Thank you for your submissions! Please see the links I provided in the brief, I really am looking for something more technical looking, like an apothecary. And want black text on a white background, not a black background, and nothing flowery.
Thank you all!!
Marisol

Target Market(s)

My clients are primarily women of all ages, but with more of a skin care focus, and no longer a cosmetic one, I would also like to appeal to a male audience. My clients are health conscious, gluten-free, natural, paleo, or vegan, etc. Target age is probably 25-55. Products are a bit high end, priced $45-65.

Industry/Entity Type

Cosmetics

Requirements
Must have
• It must at least say Marisol Thackery, or can say Marisol Thackery Beauty, but "Beauty" is not necessary. And capitalization is open, try whatever you think serves the brand. Likely slogans or taglines that can be included but are not essential: Care for your skin. Love and care for your skin. Handmade with love in the USA. Handmade in the USA. Think modern day apothecary. Small batch scotch. Something fine, but custom, handmade.
Nice to have
• I like the aesthetic of Oribel Skin Care a bit http://www.oribelhollis.example.au/
And of Dorian Valtz as shown here http://www.pinboardia.example/pin/847302915563017442/
Also of something like this that is even customizable http://www.pinboardia.example/pin/58274106392285514/
Every product is handmade in small batches, with fine ingredients, a moderate price point of around $45-$65. And I will likely begin making custom orders. So there could be a space to say when it was made, or for whom. I would like to keep the colors classic though, I probably want to stay away from the bright pink on this one.
Should not have
• As I mentioned, probably want to stay away from a lot of color. I like black vs. gray for the text, as it will show up better in editorials. I must look good, but also photograph well. Thanks!

```html
<!DOCTYPE html>
<html lang="en">
<head>
<meta charset="utf-8">
<title>Marisol Thackery – Body Serum Label</title>
<link rel="stylesheet" href="https://fonts.googleapis.com/css2?family=Josefin+Sans:wght@300;500;700&family=Special+Elite&family=Courier+Prime&display=swap">
<style>
  :root {
    --backdrop: #71726b;
    --label: #ffffff;
    --ink: #111111;
    --rule: #3a3a3a;
    --accent-dot: #2b2b2b;
  }
  * { margin: 0; padding: 0; box-sizing: border-box; }
  html, body {
    width: 1200px;
    height: 1198px;
    overflow: hidden;
    background: var(--backdrop);
  }
  .canvas {
    position: relative;
    width: 1200px;
    height: 1198px;
  }
  .label {
    position: absolute;
    left: 240px;
    top: 168px;
    width: 720px;
    height: 862px;
    background: var(--label);
    color: var(--ink);
    overflow: hidden;
  }
  .rule-h {
    position: absolute;
    left: 0;
    right: 0;
    top: 131px;
    height: 2px;
    background: var(--rule);
  }
  .rule-v {
    position: absolute;
    top: 0;
    bottom: 0;
    width: 2px;
    background: var(--rule);
  }
  .rule-v.inner { left: 606px; }
  .rule-v.outer { left: 628px; }
  .brand-name {
    position: absolute;
    right: 124px;
    top: 80px;
    font-family: "Josefin Sans", sans-serif;
    font-weight: 500;
    font-size: 37px;
    letter-spacing: 0.5px;
    line-height: 1;
    white-space: nowrap;
  }
  .product-name {
    position: absolute;
    left: 0;
    top: 0;
    width: 100%;
    height: 100%;
    font-family: "Josefin Sans", sans-serif;
    font-size: 108px;
    line-height: 1;
    font-weight: normal;
  }
  .product-name .word {
    position: absolute;
    left: 478px;
    writing-mode: vertical-rl;
    white-space: nowrap;
    transform-origin: top center;
  }
  .product-name .word-strong {
    top: 171px;
    font-weight: 700;
    transform: scaleY(0.6);
  }
  .product-name .word-light {
    top: 485px;
    font-weight: 300;
    transform: scaleY(0.6);
  }
  .product-name .divider-dot {
    position: absolute;
    left: 532px;
    top: 414px;
    width: 22px;
    height: 22px;
    border-radius: 50%;
    background: var(--accent-dot);
  }
  .tagline {
    position: absolute;
    left: 148px;
    top: 702px;
    font-family: "Special Elite", monospace;
    font-size: 18px;
    line-height: 1.45;
    letter-spacing: 1px;
    text-transform: uppercase;
  }
  .tagline .heart {
    width: 26px;
    height: 24px;
    vertical-align: -4px;
    margin-left: 2px;
  }
  .net-volume {
    position: absolute;
    left: 461px;
    top: 792px;
    font-family: "Courier Prime", monospace;
    font-size: 28px;
    line-height: 1;
    white-space: nowrap;
  }
</style>
</head>
<body>
  <main class="canvas">
    <section class="label" aria-label="Marisol Thackery body serum label">
      <div class="rule-h"></div>
      <div class="rule-v inner"></div>
      <div class="rule-v outer"></div>

      <p class="brand-name">MARISOL THACKERY</p>

      <h1 class="product-name">
        <span class="word word-strong">BODY</span>
        <span class="divider-dot" aria-hidden="true"></span>
        <span class="word word-light">SERUM</span>
      </h1>

      <p class="tagline">Handmade with<br>love in the USA<svg class="heart" viewBox="0 0 26 24" aria-hidden="true"><path d="M13 21 C4 14 2 10 3 7 C4 3 9 2 13 7 C16 2 22 2 23 6 C24 10 20 15 13 21 Z" fill="none" stroke="#111" stroke-width="1.6"/></svg></p>

      <p class="net-volume">1 ounce</p>
    </section>
  </main>
</body>
</html>
```